** Wanted ** Wordpress web design for scaffolding rental and construction company

We need a website design and must be functional to show a basic overview of what our company offers as a service. We have a domain name and a logo but we need web design. This web site should have another scaffolding rental page for construction and renovation as well as a quote section where customers can enter their personal information and also upload photos. The site% 26quot; www.corvanbuild.com% 26quot; should be intuitive, clear and classy ... The logo must be found on the site in several ways.

Target Market(s)

Professional and no professional

Coding

Coded - Design and coding required

Number of Pages Required

3 page

Font styles to use
Serif
Sans Serif
Decorative
Script

Requirements
Must have
• Our logo
Nice to have
• Slogan:% 26quot; The height% 26 # 224; port% 26 # 233; e hand% 26quot;

```html
<!DOCTYPE html>
<html lang="en">
<head>
<meta charset="utf-8">
<title>Corvanbuild – Construction and Renovation Services</title>
<link href="https://fonts.googleapis.com/css2?family=Archivo:wght@500;600;700;800&family=Roboto:wght@400;500;700&display=swap" rel="stylesheet">
<style>
:root{
  --blue:#0b8ed9;
  --dark:#1e1e22;
  --darker:#161618;
  --ink:#1b1b1d;
  --muted:#6b6b70;
  --beige:#ecebe3;
  --light:#f4f4f4;
  --white:#ffffff;
  --line:#e2e2e2;
}
*{box-sizing:border-box;margin:0;padding:0}
html,body{width:1200px;height:4796px;overflow:hidden}
body{position:relative;background:var(--white);font-family:"Roboto",Arial,sans-serif;color:var(--ink)}
.abs{position:absolute}
h1,h2,h3,h4{font-family:"Archivo","Roboto",sans-serif}
.btn{display:inline-block;background:var(--blue);color:var(--white);font:600 13px "Roboto",sans-serif;letter-spacing:.06em;text-transform:uppercase;padding:12px 30px}
.more{font:700 12px "Roboto",sans-serif;text-transform:uppercase;color:var(--ink);display:flex;align-items:center;gap:8px}

/* header */
.header{left:0;top:0;width:1200px;height:88px;background:var(--white);z-index:3}
.brand{left:0;top:0;width:180px;height:88px;background:var(--dark);display:flex;align-items:center;justify-content:center;gap:10px;color:var(--white);font:700 18px "Archivo",sans-serif}
.brand-mark{width:16px;height:16px;background:var(--blue)}
.topbar{left:200px;top:0;width:1000px;height:32px;border-bottom:1px solid var(--line);display:flex;align-items:center;gap:36px;font-size:12px;color:var(--muted);padding-left:40px}
.topbar .social{margin-left:auto;margin-right:24px;display:flex;gap:12px}
.social span{width:10px;height:10px;border-radius:50%;background:#7a7a80;display:block}
.nav{left:340px;top:32px;height:56px;display:flex;align-items:center;gap:0}
.nav a{font-size:13px;color:var(--ink);text-decoration:none;padding:0 16px;border-right:1px solid var(--line);line-height:20px}
.nav a:last-child{border-right:0}
.quote-btn{left:1052px;top:32px;width:148px;height:56px;background:var(--blue);color:var(--white);font:700 12px "Roboto",sans-serif;text-transform:uppercase;display:flex;align-items:center;justify-content:center}

/* hero */
.hero{left:0;top:88px;width:1200px;height:632px;background:linear-gradient(180deg,#7f97ab 0%,#a9b7bf 45%,#5d6a60 100%)}
.hero-title{left:0;top:348px;width:1200px;text-align:center;color:var(--white);font:700 54px/66px "Roboto",sans-serif}
.hero-btn{left:514px;top:506px;width:172px;text-align:center}

/* intro */
.intro-mark{left:578px;top:776px;width:44px;height:44px;border-radius:50%;background:var(--blue)}
.intro-title{left:0;top:870px;width:1200px;text-align:center;font:700 32px "Archivo",sans-serif}
.features{left:168px;top:996px;width:864px;display:flex;gap:44px}
.feature{width:260px}
.feature svg{display:block;margin-bottom:16px}
.feature h3{font:700 18px "Archivo",sans-serif;margin-bottom:12px}
.feature p{font-size:13px;line-height:20px;color:var(--muted)}

/* services */
.services{left:0;top:1240px;width:1200px;height:600px;background:var(--beige)}
.section-title{font:700 34px "Archivo",sans-serif}
.services .section-title{position:absolute;left:128px;top:60px}
.services .all{position:absolute;left:952px;top:72px;font-size:12px;font-weight:500}
.service-cards{position:absolute;left:128px;top:140px;display:flex;gap:24px}
.service{width:300px;background:var(--white)}
.service .photo{height:240px}
.service .body{padding:22px 24px 26px}
.service h3{font:700 16px "Archivo",sans-serif;margin-bottom:8px}
.service p{font-size:12px;line-height:18px;color:var(--muted);margin-bottom:22px}

/* partners */
.partners{left:176px;top:1920px;width:848px;display:flex;justify-content:space-between;align-items:center}
.partners span{display:block;width:150px;height:40px;background:#3a3a3e;border-radius:4px}

/* request */
.request-photo{left:0;top:2048px;width:848px;height:552px;background:linear-gradient(160deg,#9fb5c9 0%,#5f7c97 50%,#6b5a44 100%)}
.request-box{left:600px;top:2132px;width:468px;height:356px;background:var(--dark);color:var(--white);padding:56px 60px}
.request-box h2{font:700 32px "Archivo",sans-serif;margin-bottom:24px}
.request-box p{font-size:12px;line-height:20px;color:#c9c9cc;margin-bottom:34px}

/* projects */
.eyebrow{left:128px;top:2684px;font-size:13px;color:var(--muted);text-transform:uppercase}
.projects-title{left:128px;top:2708px}
.projects-text{left:760px;top:2690px;width:312px;font-size:12px;line-height:18px;color:var(--muted)}
.project-row{left:20px;top:2800px;display:flex;gap:20px}
.project{width:275px;height:400px;position:relative}
.project .card{position:absolute;left:12px;bottom:0;width:248px;background:var(--white);padding:22px 22px 26px;font:700 17px/23px "Archivo",sans-serif}
.dots{left:560px;top:3240px;display:flex;gap:8px}
.dots span{width:8px;height:8px;border-radius:50%;background:var(--ink);display:block}
.dots span.on{background:#9a9a9a}

/* testimonials */
.testimonials{left:0;top:3300px;width:1200px;height:400px;background:var(--dark);color:var(--white)}
.testimonials h2{position:absolute;left:128px;top:104px;font:700 34px/44px "Archivo",sans-serif}
.testimonials h2 em{font-style:normal;color:var(--blue)}
.t-rule{position:absolute;left:128px;top:204px;width:120px;height:2px;background:var(--blue)}
.t-arrows{position:absolute;left:128px;top:280px;display:flex;gap:12px}
.t-arrows span{width:40px;height:40px;background:var(--blue);display:flex;align-items:center;justify-content:center}
.avatar{position:absolute;left:608px;top:74px;width:72px;height:72px;border-radius:50%;background:linear-gradient(135deg,#c9a58a,#6f5242)}
.stars{position:absolute;left:608px;top:160px;display:flex;gap:3px}
.quote{position:absolute;left:608px;top:186px;width:440px;font-size:13px;line-height:21px;color:#d6d6d8}
.who{position:absolute;left:608px;top:268px;font:700 13px "Roboto",sans-serif}
.who small{display:block;font-weight:400;color:#9c9ca0;margin-top:4px}

/* news */
.news-title{left:128px;top:3766px}
.news-all{left:964px;top:3780px;font-size:12px;font-weight:500}
.news-row{left:128px;top:3840px;display:flex;gap:36px}
.news{width:288px;height:280px;background:var(--light);padding:32px 32px}
.news .meta{font-size:11px;color:var(--muted);line-height:16px;margin-bottom:30px}
.news .tag{font-size:11px;color:var(--muted);margin-bottom:6px}
.news h3{font:700 17px/22px "Archivo",sans-serif;margin-bottom:34px}

/* newsletter */
.newsletter{left:0;top:4200px;width:1200px;height:400px;background:linear-gradient(120deg,#8c8f93 0%,#d8d8d6 40%,#b9b6ae 100%)}
.news-box{left:360px;top:4280px;width:620px;height:236px;background:rgba(255,255,255,.9);text-align:center;padding-top:44px}
.news-box h2{font:700 32px "Archivo",sans-serif;margin-bottom:12px}
.news-box p{font-size:12px;color:var(--muted);margin-bottom:26px}
.subscribe{display:flex;justify-content:center}
.subscribe span{display:block;width:280px;height:40px;border:1px solid #cfcfcf;background:var(--white);font-size:12px;color:var(--muted);text-align:left;padding:12px 14px}
.subscribe b{display:block;width:96px;height:40px;background:var(--darker);color:var(--white);font:500 12px/40px "Roboto",sans-serif}

/* footer */
.footer{left:0;top:4600px;width:1200px;height:196px;background:var(--darker)}
.footer .brand{top:58px;left:96px;width:160px;height:80px;background:transparent}
.footer-nav{position:absolute;left:336px;top:88px;display:flex;gap:28px}
.footer-nav a{color:#a9a9ad;font-size:12px;text-decoration:none}
.footer-social{position:absolute;left:900px;top:91px;display:flex;gap:14px}
.footer-social span{width:10px;height:10px;border-radius:50%;background:#8b8b90;display:block}
</style>
</head>
<body>

<header class="abs header">
  <div class="abs brand"><span class="brand-mark"></span>Corvanbuild</div>
  <div class="abs topbar">
    <span>12 Harbor Lane, Westfield</span>
    <span>info@corvanbuild.com</span>
    <span>+1 (555) 014 2290</span>
    <span class="social"><span></span><span></span><span></span><span></span></span>
  </div>
  <nav class="abs nav">
    <a href="#">Home</a><a href="#">About Us</a><a href="#">Services</a><a href="#">Scaffolding Rental</a><a href="#">Contact Us</a>
  </nav>
  <div class="abs quote-btn">Request a Quote</div>
</header>

<section class="abs hero" role="img" aria-label="Glass office tower against a blue sky with palm trees"></section>
<h1 class="abs hero-title">Construction and Renovation<br>Services</h1>
<span class="abs btn hero-btn">Learn More</span>

<span class="abs intro-mark"></span>
<h2 class="abs intro-title">Height at your fingertips</h2>
<div class="abs features">
  <div class="feature">
    <svg width="36" height="36" viewBox="0 0 36 36" fill="none" stroke="#1b1b1d" stroke-width="2"><path d="M4 34V8h8v26M4 8l14-4h14v6M20 4v6M30 10v8M26 18h8M2 34h32"/></svg>
    <h3>Modern construction</h3>
    <p>Sturdy frames and skilled crews deliver safe, lasting builds on every site.</p>
  </div>
  <div class="feature">
    <svg width="36" height="36" viewBox="0 0 36 36" fill="none" stroke="#1b1b1d" stroke-width="2"><path d="M4 22h28v12H4zM4 28h28M12 22v6M22 28v6M18 22v-8M10 6l16 8M14 4l-6 6"/></svg>
    <h3>Modern renovation</h3>
    <p>Sturdy frames and skilled crews deliver safe, lasting builds on every site.</p>
  </div>
  <div class="feature">
    <svg width="36" height="36" viewBox="0 0 36 36" fill="none" stroke="#1b1b1d" stroke-width="2"><path d="M6 2v32M30 2v32M6 8h24M6 20h24M6 32h24M6 8l24 12M6 20l24 12"/></svg>
    <h3>Scaffolding rental</h3>
    <p>Sturdy frames and skilled crews deliver safe, lasting builds on every site.</p>
  </div>
</div>

<section class="abs services">
  <h2 class="section-title">Our Services</h2>
  <span class="all more">View All Services
    <svg width="12" height="10" viewBox="0 0 12 10"><path d="M0 5h10M6 1l4 4-4 4" stroke="#1b1b1d" stroke-width="2" fill="none"/></svg></span>
  <div class="service-cards">
    <article class="service">
      <div class="photo" role="img" aria-label="Building under construction with scaffolding and crane" style="background:linear-gradient(180deg,#8fb3d2,#a8845e)"></div>
      <div class="body"><h3>Construction</h3><p>Quality work from planning to handover, done on time.</p>
        <span class="more">Read More <svg width="12" height="10" viewBox="0 0 12 10"><path d="M0 5h10M6 1l4 4-4 4" stroke="#1b1b1d" stroke-width="2" fill="none"/></svg></span></div>
    </article>
    <article class="service">
      <div class="photo" role="img" aria-label="Renovated brick house wrapped in scaffolding" style="background:linear-gradient(180deg,#9fc0dc,#7a5a3e)"></div>
      <div class="body"><h3>Renovation</h3><p>Quality work from planning to handover, done on time.</p>
        <span class="more">Read More <svg width="12" height="10" viewBox="0 0 12 10"><path d="M0 5h10M6 1l4 4-4 4" stroke="#1b1b1d" stroke-width="2" fill="none"/></svg></span></div>
    </article>
    <article class="service">
      <div class="photo" role="img" aria-label="Workers on a scaffolding frame beside a building" style="background:linear-gradient(180deg,#b5835a,#5d4330)"></div>
      <div class="body"><h3>Scaffolding Rental</h3><p>Quality work from planning to handover, done on time.</p>
        <span class="more">Read More <svg width="12" height="10" viewBox="0 0 12 10"><path d="M0 5h10M6 1l4 4-4 4" stroke="#1b1b1d" stroke-width="2" fill="none"/></svg></span></div>
    </article>
  </div>
</section>

<div class="abs partners" aria-label="Partner companies"><span></span><span></span><span></span><span></span></div>

<div class="abs request-photo" role="img" aria-label="Modern glass office building with autumn trees"></div>
<div class="abs request-box">
  <h2>Request A Quote</h2>
  <p>From single homes to tall towers, we plan, supply and build with care. Tell us about your project and get a clear price.</p>
  <span class="btn">Quote Now</span>
</div>

<span class="abs eyebrow">Portfolio</span>
<h2 class="abs section-title projects-title">Our Recent Projects</h2>
<p class="abs projects-text">See the towers, offices and homes our crews have raised across the region with care and precision.</p>
<div class="abs project-row">
  <div class="project" role="img" aria-label="Dark glass skyscraper against a blue sky" style="background:linear-gradient(180deg,#2f78c4,#1a2a3d)"><div class="card">Nemo enim ipsam quia voluptas aspernatur</div></div>
  <div class="project" role="img" aria-label="Reflective glass tower seen from below" style="background:linear-gradient(180deg,#8fb6d8,#3d5a78)"><div class="card">Nemo enim ipsam quia voluptas aspernatur</div></div>
  <div class="project" role="img" aria-label="Residential tower block in black and white" style="background:linear-gradient(180deg,#d5d5d5,#2d2d2d)"><div class="card">Nemo enim ipsam quia voluptas aspernatur</div></div>
  <div class="project" role="img" aria-label="Towers at sunset" style="background:linear-gradient(180deg,#d9893e,#3a2a22)"><div class="card">Nemo enim ipsam quia voluptas aspernatur</div></div>
</div>
<div class="abs dots"><span></span><span class="on"></span><span></span><span></span><span></span></div>

<section class="abs testimonials">
  <h2>What Clients Say<br>About <em>Corvanbuild</em></h2>
  <span class="t-rule"></span>
  <div class="t-arrows">
    <span><svg width="12" height="12" viewBox="0 0 12 12"><path d="M10 6H2M6 2L2 6l4 4" stroke="#fff" stroke-width="2" fill="none"/></svg></span>
    <span><svg width="12" height="12" viewBox="0 0 12 12"><path d="M2 6h8M6 2l4 4-4 4" stroke="#fff" stroke-width="2" fill="none"/></svg></span>
  </div>
  <div class="avatar" role="img" aria-label="Client portrait"></div>
  <div class="stars">
    <svg width="70" height="12" viewBox="0 0 70 12" fill="#f2b01e"><path id="s" d="M6 0l1.8 4 4.2.4-3.2 2.8 1 4.2L6 9.2 2.2 11.4l1-4.2L0 4.4 4.2 4z"/><use href="#s" x="14"/><use href="#s" x="28"/><use href="#s" x="42"/><use href="#s" x="56"/></svg>
  </div>
  <p class="quote">“They delivered the scaffolding on time, set it up safely and kept the whole site tidy from start to finish.”</p>
  <p class="who">Lena Marsh<small>Client</small></p>
</section>

<h2 class="abs section-title news-title">Recent News</h2>
<span class="abs news-all more">View All News <svg width="12" height="10" viewBox="0 0 12 10"><path d="M0 5h10M6 1l4 4-4 4" stroke="#1b1b1d" stroke-width="2" fill="none"/></svg></span>
<div class="abs news-row">
  <article class="news"><p class="meta">by Tom Avery<br>22 Feb 2024</p><p class="tag">Construction</p><h3>Nemo enim ipsam quia voluptas sit aspernatur aut odit aut</h3><span class="more">Read More <svg width="12" height="10" viewBox="0 0 12 10"><path d="M0 5h10M6 1l4 4-4 4" stroke="#1b1b1d" stroke-width="2" fill="none"/></svg></span></article>
  <article class="news"><p class="meta">by Tom Avery<br>22 Feb 2024</p><p class="tag">Construction</p><h3>Nemo enim ipsam quia voluptas sit aspernatur aut odit aut</h3><span class="more">Read More <svg width="12" height="10" viewBox="0 0 12 10"><path d="M0 5h10M6 1l4 4-4 4" stroke="#1b1b1d" stroke-width="2" fill="none"/></svg></span></article>
  <article class="news"><p class="meta">by Tom Avery<br>22 Feb 2024</p><p class="tag">Renovation</p><h3>Nemo enim ipsam quia voluptas sit aspernatur aut odit aut</h3><span class="more">Read More <svg width="12" height="10" viewBox="0 0 12 10"><path d="M0 5h10M6 1l4 4-4 4" stroke="#1b1b1d" stroke-width="2" fill="none"/></svg></span></article>
</div>

<section class="abs newsletter" role="img" aria-label="Bright modern interior with large windows"></section>
<div class="abs news-box">
  <h2>Let's stay in touch</h2>
  <p>Subscribe to our newsletter for latest updates</p>
  <div class="subscribe"><span>Email</span><b>Subscribe</b></div>
</div>

<footer class="abs footer">
  <div class="abs brand"><span class="brand-mark"></span>Corvanbuild</div>
  <nav class="footer-nav"><a href="#">Home</a><a href="#">About Us</a><a href="#">Services</a><a href="#">Scaffolding Rental</a><a href="#">Contact Us</a></nav>
  <div class="footer-social"><span></span><span></span><span></span><span></span></div>
</footer>

</body>
</html>
```